Flyer design for webdesign company

create a flyer that can be printed or sent as an email. The flyer needs to be professional, modern and engaging.

Reason: opportunity for all designers to get their designs in.

Target Market(s)

business owners that do not have a website

Industry/Entity Type

It Company

Font styles to use
Sans Serif

```html
<!DOCTYPE html>
<html lang="en">
<head>
<meta charset="UTF-8">
<title>Web Design Flyer</title>
<link rel="stylesheet" href="https://fonts.googleapis.com/css2?family=Jost:wght@400;500;600;700;800&family=Open+Sans:wght@600;700&display=swap">
<style>
  :root {
    --orange: #f39a1f;
    --orange-deep: #ee8a12;
    --charcoal: #3c3c3e;
    --ink: #2e2e30;
    --paper: #ffffff;
    --backdrop: #d9d9db;
    --muted: #555558;
  }
  * { margin: 0; padding: 0; box-sizing: border-box; }
  html, body { width: 1200px; height: 1200px; overflow: hidden; }
  body { background: var(--backdrop); position: relative; font-family: "Jost", sans-serif; }

  .flyer {
    position: absolute; left: 197px; top: 30px;
    width: 806px; height: 1140px;
    background: var(--paper); overflow: hidden;
    box-shadow: 0 10px 30px rgba(0,0,0,.18);
  }

  .headline { position: absolute; top: 66px; left: 0; right: 0; text-align: center; white-space: nowrap; }
  .headline__kicker { font-size: 38px; font-weight: 400; color: var(--ink); letter-spacing: 1px; line-height: 1; }
  .headline__main { font-size: 68px; font-weight: 700; color: var(--orange); letter-spacing: 1px; line-height: 1.05; margin-top: 8px; }

  .team-photo {
    position: absolute; top: 228px; left: 0; width: 806px; height: 200px;
    background: linear-gradient(90deg, #c9b49a 0%, #8ba89a 25%, #c7b8ad 45%, #5a5b66 60%, #d0a9a6 78%, #6fb6d6 100%);
  }

  .price-tag {
    position: absolute; top: 428px; left: 0; width: 265px; height: 255px;
    background: var(--charcoal); text-align: center; padding-top: 28px;
  }
  .price-tag__only { font-size: 54px; font-weight: 700; color: var(--paper); line-height: 1; }
  .price-tag__amount { font-size: 124px; font-weight: 800; color: var(--orange); line-height: .95; }
  .price-tag__per { font-size: 48px; font-weight: 600; color: var(--paper); line-height: 1; }

  .benefits { position: absolute; top: 448px; left: 292px; list-style: none; }
  .benefits li {
    font-family: "Open Sans", sans-serif; font-weight: 600; font-size: 15px; color: var(--ink);
    line-height: 28px; display: flex; align-items: center; gap: 10px; white-space: nowrap;
  }
  .benefits svg { flex: none; }

  .promo-band {
    position: absolute; top: 683px; left: 0; width: 806px; height: 135px;
    background: linear-gradient(120deg, var(--orange-deep) 0%, var(--orange) 55%, #f6ab3a 100%);
    padding: 22px 0 0 42px;
  }
  .promo-band__text { font-size: 25px; font-weight: 600; color: var(--ink); line-height: 1.15; max-width: 440px; }
  .promo-band__phone { display: flex; align-items: center; gap: 10px; margin-top: 8px; font-size: 38px; font-weight: 600; color: var(--paper); line-height: 1; }

  .laptop-shot {
    position: absolute; top: 655px; left: 545px; width: 230px; height: 148px;
    background: linear-gradient(160deg, #2a3a8a 0%, #3f55a8 60%, #c9ccd3 100%);
    border-radius: 8px 8px 4px 4px;
  }

  .footer { position: absolute; top: 818px; left: 0; width: 806px; height: 282px; display: flex; align-items: center; }
  .brand { width: 300px; display: flex; flex-direction: column; align-items: center; gap: 14px; }
  .brand__mark { width: 70px; height: 70px; border-radius: 50%; background: var(--orange); }
  .brand__name { font-size: 26px; font-weight: 600; color: var(--orange); white-space: nowrap; }
  .footer__divider { width: 2px; height: 170px; background: #e2e2e4; }
  .pricing { flex: 1; text-align: center; white-space: nowrap; }
  .pricing__label { font-size: 30px; font-weight: 700; color: var(--ink); line-height: 1; }
  .pricing__amount { font-size: 46px; font-weight: 700; color: var(--orange); line-height: 1.15; margin-top: 4px; }
  .pricing__daily { font-size: 30px; font-weight: 400; color: var(--ink); line-height: 1.1; }
  .pricing__note { font-size: 20px; font-weight: 400; color: var(--muted); margin-top: 4px; }

  .base-strip { position: absolute; bottom: 0; left: 0; width: 806px; height: 40px; background: var(--charcoal); }
</style>
</head>
<body>
  <main class="flyer">
    <header class="headline">
      <p class="headline__kicker">ATTRACT MORE CUSTOMERS</p>
      <h1 class="headline__main">MAKE MORE MONEY</h1>
    </header>

    <div class="team-photo" role="img" aria-label="Photo of a row of diverse people using laptops, tablets and phones"></div>

    <div class="price-tag">
      <p class="price-tag__only">ONLY</p>
      <p class="price-tag__amount">$3</p>
      <p class="price-tag__per">A DAY</p>
    </div>

    <ul class="benefits">
      <li><svg width="14" height="12" viewBox="0 0 14 12"><path d="M1 6l4 4 8-9" fill="none" stroke="#f39a1f" stroke-width="2.5"/></svg>97% of people look online for businesses. You need a website</li>
      <li><svg width="14" height="12" viewBox="0 0 14 12"><path d="M1 6l4 4 8-9" fill="none" stroke="#f39a1f" stroke-width="2.5"/></svg>You're losing many customers by not having a website</li>
      <li><svg width="14" height="12" viewBox="0 0 14 12"><path d="M1 6l4 4 8-9" fill="none" stroke="#f39a1f" stroke-width="2.5"/></svg>Beat your competition with better visibility and credibility</li>
      <li><svg width="14" height="12" viewBox="0 0 14 12"><path d="M1 6l4 4 8-9" fill="none" stroke="#f39a1f" stroke-width="2.5"/></svg>BEAUTIFUL WEBSITES AVAILABLE NOW</li>
      <li><svg width="14" height="12" viewBox="0 0 14 12"><path d="M1 6l4 4 8-9" fill="none" stroke="#f39a1f" stroke-width="2.5"/></svg>Smart, clean website designs ($3000 Value. No extra charge)</li>
      <li><svg width="14" height="12" viewBox="0 0 14 12"><path d="M1 6l4 4 8-9" fill="none" stroke="#f39a1f" stroke-width="2.5"/></svg>Limited to ONLY 4 WEBSITES per area. Don't miss out!</li>
      <li><svg width="14" height="12" viewBox="0 0 14 12"><path d="M1 6l4 4 8-9" fill="none" stroke="#f39a1f" stroke-width="2.5"/></svg>Social Media setup options (search &amp; social networks)</li>
    </ul>

    <section class="promo-band">
      <p class="promo-band__text">Stop wasting money on mailers and print advertising.</p>
      <p class="promo-band__phone">
        <svg width="30" height="30" viewBox="0 0 30 30"><circle cx="15" cy="15" r="13" fill="none" stroke="#fff" stroke-width="2"/><path d="M10 8c-1 1-2 3 0 6s5 6 8 8c2 1 3 0 4-1l-3-3-2 1c-2-1-4-3-5-5l1-2z" fill="#fff"/></svg>
        1-800-555-0147
      </p>
    </section>

    <div class="laptop-shot" role="img" aria-label="Photo of an open laptop showing a sample business website"></div>

    <footer class="footer">
      <div class="brand">
        <span class="brand__mark"></span>
        <span class="brand__name">Novaline Sites</span>
      </div>
      <span class="footer__divider"></span>
      <div class="pricing">
        <p class="pricing__label">PRICING:</p>
        <p class="pricing__amount">ONLY $99/MONTH</p>
        <p class="pricing__daily">(THAT'S $3.30/DAY)</p>
        <p class="pricing__note">(No other costs)</p>
      </div>
    </footer>

    <div class="base-strip"></div>
  </main>
</body>
</html>
```